Construction Company Needs Letterhead Design

We recently had a new logo designed and would like to have our letterhead updated to a trendier design. We are a concrete construction company based out of Iowa, but do work for Agricultural businesses across the Midwest.

Industry/Entity Type

Construction

Colors
ec1f27
000000
ffffff

Requirements
Must have
• Must stay within our current color scheme of red/black/white. Must have have our address, phone number, e-mail address, etc. printed on the letterhead as well.

```html
<!DOCTYPE html>
<html lang="en">
<head>
<meta charset="utf-8">
<title>Harlow Letterhead</title>
<link href="https://fonts.googleapis.com/css2?family=Lato:wght@300;400;700&display=swap" rel="stylesheet">
<style>
  :root {
    --brand-red: #ec1f27;
    --brand-black: #000000;
    --paper: #ffffff;
    --ink: #1e1e1e;
    --muted: #555555;
    --backdrop: #e6e6e6;
  }
  * { margin: 0; padding: 0; box-sizing: border-box; }
  html, body {
    width: 1200px; height: 1200px; overflow: hidden;
    background: var(--backdrop);
    font-family: "Lato", sans-serif;
  }
  .letterhead {
    position: absolute;
    left: 200px; top: 34px;
    width: 800px; height: 1132px;
    background: var(--paper);
    box-shadow: 0 4px 18px rgba(0,0,0,0.12);
    overflow: hidden;
  }
  .brand {
    position: absolute; left: 70px; top: 96px;
    display: flex; align-items: center; gap: 12px;
  }
  .brand-mark {
    width: 30px; height: 30px; border-radius: 50%;
    background: var(--brand-red);
  }
  .brand-name {
    font-weight: 700; font-size: 36px; letter-spacing: 1px;
    color: var(--brand-black);
  }
  .contact {
    position: absolute; left: 520px; top: 70px;
    padding-left: 18px;
    border-left: 1px solid #999;
    font-size: 11px; line-height: 1.5; color: var(--muted);
  }
  .contact-item { display: flex; align-items: center; gap: 6px; }
  .contact-item svg { width: 9px; height: 9px; fill: var(--brand-red); }
  .letter-body {
    position: absolute; left: 70px; top: 250px; width: 600px;
    font-size: 15px; line-height: 1.75; color: var(--ink);
  }
  .salutation { margin-bottom: 22px; }
  .letter-body p { margin-bottom: 26px; }
  .signature {
    position: absolute; left: 70px; top: 830px;
  }
  .signature-mark {
    width: 120px; height: 46px; margin-bottom: 10px;
    background: linear-gradient(90deg, #f2f2f2, #e4e4e4);
  }
  .signer-name { font-size: 20px; color: var(--ink); }
  .signer-title { font-size: 14px; color: var(--muted); margin-top: 2px; }
  .footer-band {
    position: absolute; left: 0; bottom: 0; width: 100%; height: 12px;
    display: flex;
  }
  .footer-band .band-red { flex: 0 0 74%; background: var(--brand-red); }
  .footer-band .band-black { flex: 1; background: var(--brand-black); }
</style>
</head>
<body>
  <main class="letterhead">
    <header>
      <div class="brand">
        <span class="brand-mark"></span>
        <span class="brand-name">HARLOW</span>
      </div>
      <address class="contact">
        <div>12 Granary Road, Fieldview</div>
        <div>P.O. Box 410, Cedar Falls</div>
        <div class="contact-item">
          <svg viewBox="0 0 10 10"><path d="M2 0.5 L4 2.5 L3 4 Q4.5 6 6 7 L7.5 6 L9.5 8 L8 9.5 Q3.5 9 0.5 2 Z"/></svg>
          555-0142-7781
        </div>
        <div class="contact-item">
          <svg viewBox="0 0 10 10"><rect x="0.5" y="2" width="9" height="6" rx="1"/></svg>
          hello@harlowco.com
        </div>
        <div class="contact-item">
          <svg viewBox="0 0 10 10"><circle cx="5" cy="5" r="4.5"/></svg>
          www.harlowco.com
        </div>
      </address>
    </header>

    <section class="letter-body">
      <div class="salutation">Dear Mr. Smith,</div>
      <p>Lorem ipsum dolor sit amet, consectetur adipiscing elit. Donec orci purus, luctus vitae dignissim eu, iaculis sed purus. Vivamus faucibus, ipsum nec aliquet viverra, leo mauris condimentum ligula, sit amet sagittis enim ligula quis arcu. Nam egestas tortor id nisi porttitor mattis. In tortor ante, ultricies in suscipit a, tempus non massa. Vivamus et auctor mi. Fusce vel massa nulla. Phasellus nec eros mauris, et scelerisque orci. Donec malesuada orci vitae nulla accumsan porta a id massa. Quisque accumsan iaculis magna sit amet fringilla. Maecenas consequat, magna eget tincidunt semper, odio nibh rutrum mi, id feugiat ante nisi eu risus. Vestibulum nunc orci, rhoncus a placerat in, ultricies in mi. Cras mattis varius eros, vel fringilla nisi suscipit eget.</p>
      <p>Quisque scelerisque sagittis nulla at porttitor. Mauris a justo et tellus interdum tristique. Sed id augue vitae urna euismod commodo aliquet a quam. Pellentesque arcu velit, cursus et malesuada ut, consequat et diam. Nullam erat sem, rhoncus id ullamcorper vitae, rhoncus et arcu. In ultricies ultricies nulla, ut rutrum nisi iaculis at. Donec eu magna a metus ornare faucibus. Fusce aliquet faucibus ultricies. Morbi semper, est id tincidunt gravida, sem arcu adipiscing lacus, ac bibendum nulla leo eu purus. Quisque nec diam sed risus consectetur accumsan quis quis nibh. Vestibulum id purus lorem.</p>
    </section>

    <footer class="signature">
      <div class="signature-mark" role="img" aria-label="Handwritten signature"></div>
      <div class="signer-name">John Doe</div>
      <div class="signer-title">Co-Founder &amp; CEO</div>
    </footer>

    <div class="footer-band" aria-hidden="true">
      <span class="band-red"></span>
      <span class="band-black"></span>
    </div>
  </main>
</body>
</html>
```